Family Values Poster

Need a poster for my kids (ages 5-8) that says:
Be Smart
Be Kind
Be Curious
Be Grateful
We Love You

fun, but hopefully something that they will keep for a long time

Target Market(s)

my kids

Requirements
Must have
• vertical
Nice to have
• fun and attention grabbing
Should not have
• look cheesy - not a generic inspirational poster

```html
<!DOCTYPE html>
<html lang="en">
<head>
<meta charset="utf-8">
<title>Family Values Poster</title>
<link href="https://fonts.googleapis.com/css2?family=Fredoka:wght@500&family=Montserrat:wght@800&family=Great+Vibes&display=swap" rel="stylesheet">
<style>
  :root {
    --stage: #b9bbb8;
    --paper: #ffffff;
    --sky: #b3e0f7;
    --sun: #f9ad1a;
    --green: #8cc63f;
    --pink: #ec4b6b;
    --orange: #f4701f;
    --purple: #8e5bb4;
    --star: #f1d27a;
    --star-edge: #b58a2c;
    --script: #b3e0f7;
  }
  html, body { margin: 0; padding: 0; overflow: hidden; }
  body {
    width: 1200px; height: 1200px;
    background: var(--stage);
    position: relative;
  }
  .poster {
    position: absolute;
    left: 400px; top: 20px;
    width: 400px; height: 1160px;
    background: var(--paper);
    overflow: hidden;
  }
  .poster-shapes { position: absolute; inset: 0; }
  .values {
    position: absolute;
    left: 46px; top: 92px;
    margin: 0; padding: 0; list-style: none;
    font-family: "Fredoka", sans-serif;
    font-weight: 500;
    font-size: 60px;
    line-height: 66px;
    letter-spacing: -2px;
  }
  .values .smart { color: var(--green); }
  .values .kind { color: var(--pink); }
  .values .curious { color: var(--orange); }
  .values .grateful { color: var(--purple); }
  .sign-off {
    position: absolute;
    left: 44px; top: 920px;
    width: 340px; height: 200px;
    margin: 0;
  }
  .sign-off .we-love {
    position: absolute; left: 0; top: 0;
    font-family: "Montserrat", sans-serif;
    font-weight: 800;
    font-size: 70px;
    letter-spacing: -2px;
    color: var(--paper);
    transform: rotate(-6deg);
    transform-origin: left top;
    line-height: 1;
  }
  .sign-off .you {
    position: absolute; left: 70px; top: 40px;
    font-family: "Great Vibes", cursive;
    font-weight: 400;
    font-size: 120px;
    color: var(--script);
    transform: rotate(-6deg);
    line-height: 1;
  }
</style>
</head>
<body>
  <main class="poster">
    <svg class="poster-shapes" viewBox="0 0 400 1160" width="400" height="1160" aria-hidden="false">
      <defs>
        <linearGradient id="family-tones" x1="0" y1="0" x2="1" y2="1">
          <stop offset="0" stop-color="#e9a079"/>
          <stop offset="0.5" stop-color="#f07a4a"/>
          <stop offset="1" stop-color="#4bb3c0"/>
        </linearGradient>
      </defs>
      <!-- sky band with cloud edge -->
      <rect class="sky-band" x="0" y="430" width="400" height="730" fill="var(--sky)"/>
      <g class="cloud-edge" fill="var(--paper)">
        <rect x="0" y="380" width="400" height="55"/>
        <circle cx="30" cy="430" r="42"/>
        <circle cx="120" cy="438" r="50"/>
        <circle cx="225" cy="430" r="48"/>
        <circle cx="330" cy="424" r="52"/>
      </g>
      <!-- family illustration area -->
      <rect class="family-illustration" role="img" aria-label="Illustration of four smiling children standing together, one holding a red balloon, with a butterfly nearby"
            x="40" y="380" width="340" height="470" rx="24" fill="url(#family-tones)" opacity="0.55"/>
      <!-- sunny footer with cloud top -->
      <g class="sun-band" fill="var(--sun)">
        <rect x="0" y="930" width="400" height="230"/>
        <circle cx="80" cy="950" r="80"/>
        <circle cx="200" cy="915" r="70"/>
        <circle cx="320" cy="890" r="85"/>
        <rect x="300" y="880" width="100" height="60"/>
      </g>
      <!-- stars -->
      <g class="stars" fill="var(--star)" stroke="var(--star-edge)" stroke-width="1.5" stroke-linejoin="round">
        <polygon points="46,38 53,58 74,58 57,70 63,90 46,78 29,90 35,70 18,58 39,58"/>
        <polygon points="290,173 293,182 303,182 295,188 298,197 290,191 282,197 285,188 277,182 287,182"/>
        <polygon points="58,390 61,399 71,399 63,405 66,414 58,408 50,414 53,405 45,399 55,399"/>
      </g>
    </svg>

    <ul class="values">
      <li class="smart">Be Smart</li>
      <li class="kind">Be Kind</li>
      <li class="curious">Be Curious</li>
      <li class="grateful">Be Grateful</li>
    </ul>

    <p class="sign-off">
      <span class="we-love">WE LOVE</span>
      <span class="you">You</span>
    </p>
  </main>
</body>
</html>
```